JT Holly Cleaning Business Card

We need a business card for our new business, a cleaning company using steam. We already have a logo, and would like a modern-looking card using colors that go well with those in our logo.

```html
<!DOCTYPE html>
<html lang="en">
<head>
<meta charset="utf-8">
<title>JT Holly Cleaning Business Card</title>
<link rel="stylesheet" href="https://fonts.googleapis.com/css2?family=Open+Sans:wght@400;600;700&display=swap">
<style>
  :root {
    --stage: #e6e8ec;
    --blue: #3b4fa3;
    --blue-deep: #2c3b8c;
    --blue-light: #4a62b5;
    --green: #7cc242;
    --ink: #1e1e1e;
    --white: #ffffff;
  }
  * { margin: 0; padding: 0; box-sizing: border-box; }
  html, body {
    width: 1200px; height: 680px; overflow: hidden;
    background: var(--stage);
    font-family: "Open Sans", Verdana, sans-serif;
  }
  .canvas { position: relative; width: 1200px; height: 680px; }
  .card {
    position: absolute; top: 197px;
    width: 500px; height: 286px;
    border-radius: 3px; overflow: hidden;
    box-shadow: 0 6px 18px rgba(0,0,0,0.18);
  }
  /* Front */
  .card-front { left: 70px; background: var(--white); }
  .card-front .base-band {
    position: absolute; left: 0; right: 0; bottom: 0; height: 12px;
    background: var(--blue);
  }
  .brand { position: absolute; display: flex; align-items: center; }
  .brand-dot { border-radius: 50%; background: var(--green); flex: none; }
  .brand-name { font-weight: 700; line-height: 1.05; }
  .card-front .brand { left: 200px; top: 30px; gap: 10px; }
  .card-front .brand-dot { width: 40px; height: 40px; }
  .card-front .brand-name { color: var(--blue); font-size: 21px; }
  .person { position: absolute; left: 40px; top: 94px; }
  .person-name { font-size: 15px; line-height: 20px; color: var(--ink); letter-spacing: 0.5px; }
  .person-role { font-size: 13px; line-height: 18px; color: var(--green); }
  .address {
    position: absolute; left: 40px; top: 148px;
    font-size: 13px; line-height: 17px; color: var(--ink); font-style: normal;
  }
  .contacts { position: absolute; left: 40px; top: 188px; font-size: 13px; color: var(--ink); list-style: none; }
  .contacts li { display: flex; align-items: center; gap: 9px; height: 17px; line-height: 17px; }
  .contacts li.gap { margin-top: 6px; }
  .contacts svg { width: 12px; height: 12px; flex: none; }
  /* Back */
  .card-back {
    left: 630px;
    background: linear-gradient(135deg, var(--blue-light) 0%, var(--blue) 45%, var(--blue-deep) 100%);
  }
  .card-back .brand { left: 96px; top: 92px; gap: 16px; }
  .card-back .brand-dot { width: 72px; height: 72px; }
  .card-back .brand-name { color: var(--white); font-size: 34px; }
  .web {
    position: absolute; left: 0; right: 0; top: 206px; text-align: center;
    color: var(--white); font-size: 13px; letter-spacing: 4px;
  }
</style>
</head>
<body>
<main class="canvas">
  <section class="card card-front" aria-label="Business card front">
    <div class="brand">
      <span class="brand-dot"></span>
      <span class="brand-name">JT Holly<br>Cleaning</span>
    </div>
    <div class="person">
      <p class="person-name">MARK ELLISON</p>
      <p class="person-role">Manager</p>
    </div>
    <address class="address">
      1470 Birch Row Ln<br>Alden TX 78100
    </address>
    <ul class="contacts">
      <li>
        <svg viewBox="0 0 12 12" aria-label="Phone"><circle cx="6" cy="6" r="6" fill="var(--green)"/><path d="M4 3.2c-.6.4-.8 1.2-.3 2.3.6 1.4 1.7 2.6 3 3.2.9.4 1.6.2 2-.3l-.9-1-.8.4c-.7-.3-1.4-1-1.7-1.8l.4-.8z" fill="#fff"/></svg>
        512 004 2290
      </li>
      <li>
        <svg viewBox="0 0 12 12" aria-label="Fax"><circle cx="6" cy="6" r="6" fill="var(--green)"/><rect x="3" y="5" width="6" height="3.4" rx=".5" fill="#fff"/><rect x="4" y="3" width="4" height="2" fill="#fff"/></svg>
        512 004 2291
      </li>
      <li class="gap">
        <svg viewBox="0 0 12 12" aria-label="Email"><circle cx="6" cy="6" r="6" fill="var(--green)"/><rect x="2.8" y="3.8" width="6.4" height="4.4" fill="#fff"/><path d="M2.8 3.8 6 6.4 9.2 3.8" fill="none" stroke="var(--green)" stroke-width=".8"/></svg>
        info@jthollyclean.com
      </li>
      <li>
        <svg viewBox="0 0 12 12" aria-label="Website"><circle cx="6" cy="6" r="6" fill="var(--green)"/><g fill="none" stroke="#fff" stroke-width=".7"><circle cx="6" cy="6" r="3.6"/><ellipse cx="6" cy="6" rx="1.6" ry="3.6"/><path d="M2.4 6h7.2"/></g></svg>
        www.jthollyclean.com
      </li>
    </ul>
    <div class="base-band"></div>
  </section>

  <section class="card card-back" aria-label="Business card back">
    <div class="brand">
      <span class="brand-dot"></span>
      <span class="brand-name">JT Holly<br>Cleaning</span>
    </div>
    <p class="web">www.jthollyclean.com</p>
  </section>
</main>
</body>
</html>
```